KT Crewing business card

Require business card which includes:
Company name: KT CREWING PTY LTD
Email: Mick@ktcrewing.com.au
Phone: 0431 556 208
ACN: 517 238 649

slogan: Onsite Auto Electrician Labour hire

Details and logo on top side
Logo only on bottom side

colour codes : #F15A29 , #939598

Target Market(s)

Western Australia mining sector

Industry/Entity Type

Mining

Contact Information for Business Card

Require business card which includes: Company name: KT CREWING PTY LTD Email: Mick@ktcrewing.com.au Phone: 0431 556 208 ACN: 517 238 649 slogan: Onsite Auto Electrician Labour hire Details and logo on top side Logo only on bottom side colour codes : #F15A29 , #939598

Colors
EE7325
F08F49
F5BC92
FAE3D3
FDF4ED

Requirements
Must have
• double sided

```html
<!DOCTYPE html>
<html lang="en">
<head>
<meta charset="utf-8">
<title>KT Crewing – Business Card</title>
<link rel="stylesheet" href="https://fonts.googleapis.com/css2?family=Exo+2:wght@600;700;800&family=Open+Sans:wght@400;600&display=swap">
<style>
  :root {
    --orange: #F15A29;
    --grey: #939598;
    --card-black: #0c0c0c;
    --page-bg: #d9d9da;
    --white: #ffffff;
    --ink: #1a1a1a;
  }
  * { margin: 0; padding: 0; box-sizing: border-box; }
  html, body {
    width: 1200px; height: 900px; overflow: hidden;
    background: var(--page-bg);
  }
  .sheet {
    position: relative; width: 1200px; height: 900px;
  }
  .card {
    position: absolute; left: 240px; width: 720px; height: 411px;
    background: var(--card-black);
    overflow: hidden;
  }
  .card--front { top: 30px; }
  .card--back { top: 464px; }

  /* Brand */
  .brand-name {
    font-family: "Exo 2", sans-serif; font-weight: 800;
    color: var(--orange); line-height: 1; white-space: nowrap;
    display: flex; align-items: center; gap: 12px;
  }
  .brand-mark {
    width: 20px; height: 20px; background: var(--grey); flex: none;
  }

  /* Front */
  .card--front .brand-name {
    position: absolute; left: 40px; top: 192px; width: 290px;
    font-size: 42px;
  }
  .divider {
    position: absolute; left: 352px; top: 70px; width: 1px; height: 190px;
    background: var(--grey); opacity: .55;
  }
  .details {
    position: absolute; left: 384px; top: 74px; width: 310px;
    font-family: "Open Sans", sans-serif; color: var(--white);
  }
  .person-name {
    font-family: "Exo 2", sans-serif; font-weight: 700;
    color: var(--orange); font-size: 24px; letter-spacing: .5px; line-height: 1.1;
  }
  .person-role { font-size: 15px; margin-bottom: 16px; }
  .contact-line {
    display: flex; align-items: center; gap: 10px;
    font-size: 16px; margin-bottom: 4px; white-space: nowrap;
  }
  .contact-line svg { width: 16px; height: 16px; flex: none; }
  .company-number { margin-top: 24px; font-size: 16px; }
  .company-number .label { color: var(--orange); }
  .slogan-band {
    position: absolute; left: 0; right: 0; top: 284px; height: 62px;
    background: var(--grey);
    display: flex; align-items: center; justify-content: center;
  }
  .slogan {
    font-family: "Exo 2", sans-serif; font-weight: 700;
    font-size: 27px; color: var(--ink); letter-spacing: .3px;
  }

  /* Back */
  .card--back .brand-name {
    position: absolute; left: 0; right: 0; top: 0; bottom: 0;
    justify-content: center; font-size: 76px; gap: 16px;
  }
  .card--back .brand-mark { width: 34px; height: 34px; }
</style>
</head>
<body>
<main class="sheet">

  <section class="card card--front" aria-label="Business card front">
    <div class="brand-name"><span class="brand-mark"></span>KT Crewing</div>
    <div class="divider"></div>
    <div class="details">
      <p class="person-name">MARCUS REILLY</p>
      <p class="person-role">Managing Director</p>
      <p class="contact-line">
        <svg viewBox="0 0 24 24" aria-hidden="true"><path fill="var(--orange)" d="M6.6 10.8a15.1 15.1 0 0 0 6.6 6.6l2.2-2.2a1 1 0 0 1 1-.25 11.4 11.4 0 0 0 3.6.57 1 1 0 0 1 1 1V20a1 1 0 0 1-1 1A17 17 0 0 1 3 4a1 1 0 0 1 1-1h3.5a1 1 0 0 1 1 1c0 1.25.2 2.45.57 3.57a1 1 0 0 1-.25 1z"/></svg>
        0431 556 208
      </p>
      <p class="contact-line">
        <svg viewBox="0 0 24 24" aria-hidden="true"><path fill="var(--orange)" d="M2 5h20v14H2z"/><path fill="none" stroke="var(--card-black)" stroke-width="1.6" d="M2 5l10 8 10-8M2 19l7.5-7.5M22 19l-7.5-7.5"/></svg>
        Mick@ktcrewing.com.au
      </p>
      <p class="company-number"><span class="label">ACN:</span> 517 238 649</p>
    </div>
    <div class="slogan-band">
      <p class="slogan">Onsite Auto Electrician Labour hire</p>
    </div>
  </section>

  <section class="card card--back" aria-label="Business card back">
    <div class="brand-name"><span class="brand-mark"></span>KT Crewing</div>
  </section>

</main>
</body>
</html>
```